LA Billboard Project for Brisk Lending

We are running three different billboards around LA, and we need someone to take the mock-ups I've created and bring this campaign to life. Whatever wording is on the mock-ups should stay the same in the ads you create, but feel free to get creative with layout and style. I've attached our mock-ups, our style guide, our logo, and the necessary specs for the billboards. If you have any questions, feel free to reach out!

```html
<!DOCTYPE html>
<html lang="en">
<head>
<meta charset="utf-8">
<title>Brisk Lending – Billboard</title>
<link href="https://fonts.googleapis.com/css2?family=Hind:wght@400;600&display=swap" rel="stylesheet">
<style>
  :root {
    --navy: #1d2c5b;
    --yellow: #fbdd00;
    --cyan: #4cc2dc;
    --white: #ffffff;
    --stage: #262626;
    --photo-top: #c9d3dc;
    --photo-mid: #8b8f94;
    --photo-low: #4e5155;
  }
  html, body {
    margin: 0;
    padding: 0;
    width: 720px;
    height: 1200px;
    overflow: hidden;
    background: var(--stage);
  }
  .canvas {
    position: relative;
    width: 720px;
    height: 1200px;
  }
  .billboard {
    position: absolute;
    left: 20px;
    top: 443px;
    width: 680px;
    height: 313px;
    box-shadow: 0 14px 30px rgba(0,0,0,0.55);
  }
  .billboard svg { display: block; width: 100%; height: 100%; }
  .brand-name { font-family: "Hind", sans-serif; font-weight: 600; fill: var(--cyan); }
  .headline { font-family: "Hind", sans-serif; font-size: 37px; letter-spacing: 0.5px; }
  .headline .strong-yellow { font-weight: 600; fill: var(--yellow); }
  .headline .plain-white { font-weight: 400; fill: var(--white); }
  .headline .strong-cyan { font-weight: 600; fill: var(--cyan); }
  .web-address { font-family: "Hind", sans-serif; font-weight: 600; font-size: 40px; fill: var(--navy); }
</style>
</head>
<body>
<main class="canvas">
  <section class="billboard" aria-label="Brisk Lending billboard">
    <svg viewBox="0 0 1018 468" xmlns="http://www.w3.org/2000/svg">
      <defs>
        <linearGradient id="trafficTone" x1="0" y1="0" x2="0" y2="1">
          <stop offset="0" stop-color="var(--photo-top)"/>
          <stop offset="0.45" stop-color="var(--photo-mid)"/>
          <stop offset="1" stop-color="var(--photo-low)"/>
        </linearGradient>
      </defs>

      <rect class="backdrop" width="1018" height="468" fill="var(--navy)"/>

      <rect class="traffic-photo" role="img" aria-label="Photo of a congested motorway with cars and tanker trucks queued under a motorway message sign"
            x="480" y="0" width="538" height="468" fill="url(#trafficTone)"/>

      <polygon class="chevron-cyan" points="480,0 645,234 480,468" fill="var(--cyan)"/>
      <polygon class="panel-navy" points="0,0 493,0 597,234 493,468 0,468" fill="var(--navy)"/>
      <polygon class="wedge-top" points="493,0 680,0 600,234" fill="var(--yellow)"/>
      <polygon class="wedge-bottom" points="600,234 680,468 493,468" fill="var(--yellow)"/>

      <g class="brand">
        <rect x="46" y="62" width="22" height="22" fill="var(--cyan)"/>
        <text class="brand-name" x="80" y="86" font-size="40">Brisk Lending</text>
      </g>

      <rect class="headline-rule" x="45" y="178" width="4" height="128" fill="var(--yellow)"/>
      <text class="headline">
        <tspan class="strong-yellow" x="73" y="210">TRAFFIC IS A MESS.</tspan>
        <tspan class="plain-white" x="73" y="257">YOUR MORTGAGE</tspan>
        <tspan class="strong-cyan" x="73" y="304">DOESN’T HAVE TO BE.</tspan>
      </text>

      <polygon class="url-band" points="0,353 425,353 395,425 0,425" fill="var(--yellow)"/>
      <g class="globe-icon" fill="none" stroke="var(--navy)" stroke-width="2.5">
        <circle cx="62" cy="389" r="15" fill="var(--navy)"/>
        <ellipse cx="62" cy="389" rx="6" ry="15" stroke="var(--yellow)" stroke-width="2"/>
        <line x1="47" y1="389" x2="77" y2="389" stroke="var(--yellow)" stroke-width="2"/>
        <line x1="50" y1="381" x2="74" y2="381" stroke="var(--yellow)" stroke-width="1.6"/>
        <line x1="50" y1="397" x2="74" y2="397" stroke="var(--yellow)" stroke-width="1.6"/>
      </g>
      <text class="web-address" x="92" y="403">briskrefi.com</text>
    </svg>
  </section>
</main>
</body>
</html>
```